Website Redesign for Technology Focused Investment Bank

We need a website redesign for a technology and digital media focused investment banking firm. Think modern and forward thinking yet stable and smart. We provide mergers and acquisitions advisory services to our clients. Our target market are CEO's and CFO's (senior executives) that run and operate technology firms.

Larkstone Capital Partners - www.larkstonecapitalpartners.example

We are headquartered in Los Angeles, CA. Please do NOT use the Pemberly marker for anything.

We have the content and can update the photos as well.

We are looking for a "template" website we can update and edit with ease.

A competitive firm's website is: www.brackenhale.example Not sure I like it but I want it to look way better then this one.

Looking for a more modern version. Not too stuffy and conservative, please. Elegant, smart, updated and progressive/modern.
Updates

Color preferences:  Blue's including matching logo color. Grey's. You can add other colors if it flows well and looks clean and nice.

Menu:  Drop Down

Open to platform...please use one that most people can use, is reasonably priced if I need to buy it, and easy to update monthly and sometimes weekly.

Please use this website as a good example of what we are looking for (or similar version of it): www.quelmora.example

Thanks!
Derek P.

We are reviewing all submissions and will select one this week. Thank you everyone for your outstanding and creative designs you have sent us. We really appreciate it.

Thanks for everyone's hard work and creative input into our website design. We really appreciate it!

Target Market(s)

CEO's and CFO's, Entrepreneurs and Board Members of Technology Companies.

Industry/Entity Type

Investment

Font styles to use
Sans Serif

Colors
33a6d7
0492cd
0555a3
3176b5
85abd2
333333
5c5c5c
757575

Requirements
Must have
• Links to social media including Twitter, LinkedIn, Google+, Facebook, etc.

Must try to match logo color
Should not have
• No conservative, old looking colors or background. For example, no green marble look.

```html
<!DOCTYPE html>
<html lang="en">
<head>
<meta charset="utf-8">
<title>Larkstone Capital Partners</title>
<link href="https://fonts.googleapis.com/css2?family=Open+Sans:wght@400;600&family=Roboto+Condensed:wght@400;700&display=swap" rel="stylesheet">
<style>
:root{
  --navy:#0b2157;
  --topbar:#0a3a8a;
  --blue:#0555a3;
  --link:#0492cd;
  --sky:#33a6d7;
  --nav:#a5c5e1;
  --pale:#cde6f3;
  --grey-band:#f2f2f2;
  --text:#5c5c5c;
  --dark:#333333;
  --muted:#757575;
}
*{margin:0;padding:0;box-sizing:border-box}
html,body{width:804px;height:1200px;overflow:hidden;background:#fff}
body{position:relative;font-family:"Open Sans",sans-serif;color:var(--text);font-size:9.5px}
a{text-decoration:none;color:inherit}
.abs{position:absolute}
.topbar{left:0;top:0;width:804px;height:25px;background:var(--topbar)}
.toplinks{right:94px;top:7px;display:flex;gap:14px;color:#dbe7f6;font-size:9.5px;align-items:center}
.flags{display:flex;gap:4px;margin-left:4px}
.flags span{width:16px;height:11px;background:linear-gradient(#c33 0 33%,#fff 33% 66%,#24408e 66%)}
.brand{left:94px;top:0;width:172px;height:66px;background:#fff;display:flex;align-items:center;gap:8px;padding-left:10px}
.brand-mark{width:38px;height:38px;border-radius:50%;background:var(--blue)}
.brand-name{font-family:"Open Sans",sans-serif;font-size:12.5px;line-height:15px;color:var(--blue);font-weight:600}
.search{left:527px;top:40px;width:183px;height:23px;border:1px solid #c9d9ea;display:flex}
.search span{flex:1;padding:5px 7px;color:#999;font-size:9px}
.search b{width:33px;margin:2px;background:#cfe0f1;color:var(--blue);font-weight:400;font-size:11px;text-align:center;line-height:19px}
.nav{left:0;top:76px;width:804px;height:28px;background:var(--nav);display:flex;gap:15px;padding-left:105px;align-items:center;color:#fff;font-size:9px;text-transform:uppercase;font-weight:600}
.hero{left:0;top:104px;width:804px;height:284px;background:linear-gradient(180deg,#27518f 0%,#6d8fbd 40%,#8b8a6a 62%,#2c3440 100%)}
.hero-text{left:178px;top:200px;color:#fff;font-family:"Roboto Condensed",sans-serif}
.hero-text em{font-size:17px;font-style:italic;display:block}
.hero-text h1{font-size:37px;line-height:38px;font-weight:400;letter-spacing:-.5px}
.arrow{top:226px}
h2{font-family:"Roboto Condensed",sans-serif;font-weight:400;color:var(--blue);font-size:20px}
.services-title{left:0;top:403px;width:804px;text-align:center}
.service{top:444px;width:150px;text-align:center;font-family:"Roboto Condensed",sans-serif;color:var(--dark);font-size:13px}
.service .ring{width:62px;height:62px;margin:0 auto 10px;border-radius:50%;box-shadow:-3px -2px 0 #e6e6e6;display:flex;align-items:center;justify-content:center}
.divider{left:94px;top:568px;width:616px;height:3px;background:#eef1f4}
.why-photo{left:94px;top:597px;width:120px;height:131px;border:1px solid #ddd;padding:5px;background:#fff}
.why-photo div{width:100%;height:100%;background:linear-gradient(180deg,#c9ced6,#7e8ea3 55%,#3d3d44)}
.why{left:227px;top:594px;width:305px;line-height:14.5px;font-size:9.5px}
.why p{margin-top:9px}
.why a,.news a{color:var(--link)}
.readmore{display:block;margin-top:13px}
.news{left:551px;top:594px;width:160px;font-size:9.5px;line-height:14.5px}
.news li{list-style:none;margin-top:9px;padding-left:10px;position:relative}
.news li::before{content:"→";position:absolute;left:0;color:#999;font-size:7px}
.clients{left:0;top:777px;width:804px;height:89px;background:var(--grey-band)}
.client{top:813px;width:130px;text-align:center;font-family:"Roboto Condensed",sans-serif;font-weight:700;font-size:19px;color:#a8a8a8}
.tweet{left:0;top:866px;width:804px;height:117px;background:var(--pale)}
.tweet-handle{left:0;top:889px;width:804px;text-align:center;color:var(--link);font-size:9.5px}
.tweet-body{left:170px;top:909px;width:494px;text-align:center;line-height:13px}
.tweet-icon{left:131px;top:910px;width:30px;height:28px;border-radius:50%;background:#1b7bc4}
.dots{left:375px;top:950px;display:flex;gap:3px}
.dots span{width:8px;height:8px;border-radius:50%;background:#fff}
.dots span:first-child{background:var(--blue)}
.footer{left:0;top:983px;width:804px;height:217px;background:var(--navy);color:#d6deed}
.col-h{font-family:"Roboto Condensed",sans-serif;color:#fff;font-size:13px;font-weight:700}
.vline{top:990px;width:1px;height:130px;background:#1b2f66}
.email{left:94px;top:1057px;width:192px;height:24px;display:flex}
.email span{flex:1;background:#fff;color:#888;padding:6px 6px;font-size:9px}
.email b{width:62px;background:var(--link);color:#fff;display:flex;align-items:center;justify-content:center;gap:5px;font-size:12px}
.social{left:347px;top:1031px;display:flex;gap:6px}
.social span{width:23px;height:23px;border:1.5px solid #fff;border-radius:50%;color:#fff;font-size:7px;font-weight:600;display:flex;align-items:center;justify-content:center}
.contact{left:510px;top:1026px;line-height:16px;font-size:9.3px}
.contact a{color:var(--sky)}
.footnav{left:94px;top:1131px;width:616px;display:flex;justify-content:space-between;color:#fff;font-size:9.5px}
.fline{left:94px;top:1153px;width:616px;height:1px;background:#1b2f66}
.copy{left:0;top:1172px;width:804px;text-align:center;color:#fff;font-size:8px}
</style>
</head>
<body>
<div class="abs topbar"></div>
<nav class="abs toplinks"><a>Home</a><a>About Us</a><a>Contact Us</a><span class="flags"><span></span><span></span><span></span></span></nav>
<a class="abs brand"><span class="brand-mark"></span><span class="brand-name">Larkstone<br>Capital Partners</span></a>
<div class="abs search"><span>Search here...</span><b>Go</b></div>
<nav class="abs nav"><a>Services</a><a>Transactions</a><a>Research</a><a>Private Equity</a><a>Recommendations</a><a>About the Founder</a><a>Careers</a><a>News &amp; Blog</a></nav>

<div class="abs hero" role="img" aria-label="Photo of a modern glass office building seen through tall windows, sky and reflecting pool"></div>
<div class="abs hero-text"><em>WE ARE</em><h1>TECHNOLOGY AND DIGITAL<br>MEDIA INDUSTRY M&amp;A EXPERTS</h1></div>
<svg class="abs arrow" style="left:40px" width="24" height="42" viewBox="0 0 24 42"><path d="M22 1 2 21l20 20" fill="none" stroke="#fff" stroke-width="1.5"/></svg>
<svg class="abs arrow" style="left:740px" width="24" height="42" viewBox="0 0 24 42"><path d="M2 1l20 20L2 41" fill="none" stroke="#fff" stroke-width="1.5"/></svg>

<h2 class="abs services-title">Our Services</h2>
<div class="abs service" style="left:70px"><div class="ring" style="background:var(--blue)"><svg width="34" height="34" viewBox="0 0 34 34"><path d="M6 14l11-6 11 6v12l-11 6-11-6z" fill="#fff"/><circle cx="17" cy="12" r="7" fill="#fff" stroke="#0555a3" stroke-width="2"/><circle cx="17" cy="12" r="2.5" fill="#0555a3"/></svg></div>Software</div>
<div class="abs service" style="left:240px"><div class="ring" style="background:#7cc8ea"><svg width="32" height="32" viewBox="0 0 32 32" stroke="#fff" stroke-width="3" stroke-linecap="round"><path d="M6 26 24 8M8 6l18 18"/></svg></div>IT Services</div>
<div class="abs service" style="left:418px"><div class="ring" style="background:#7cc8ea"><svg width="34" height="34" viewBox="0 0 34 34" fill="none" stroke="#fff" stroke-width="2"><circle cx="17" cy="17" r="13"/><ellipse cx="17" cy="17" rx="6" ry="13"/><path d="M4 17h26"/></svg></div>Internet &amp; Digital Media</div>
<div class="abs service" style="left:583px"><div class="ring" style="background:#7cc8ea"><svg width="20" height="32" viewBox="0 0 20 32"><rect x="1" y="1" width="18" height="30" rx="2" fill="#fff"/><rect x="4" y="5" width="12" height="10" fill="#7cc8ea"/></svg></div>Mobile</div>

<div class="abs divider"></div>
<div class="abs why-photo"><div role="img" aria-label="Photo of a bright modern office lounge with bar seating"></div></div>
<section class="abs why">
  <h2>Why Us?</h2>
  <p>We are an independent investment bank and M&amp;A advisory firm focused exclusively on the global Technology and Digital Media sectors. Specifically, we execute mergers and acquisitions for the <a>Software</a>, <a>IT Services</a>, <a>Internet and Digital Media</a> industry sectors.</p>
  <p>Our professionals have completed over $20 billion in transactions to date and have experience in investment banking,</p>
  <a class="readmore">Read more...</a>
</section>
<section class="abs news">
  <h2>Latest News</h2>
  <ul>
    <li><a>July, 24 2014</a><br>Lorem Ipsum is simply dummy text of the printing and typesetting...</li>
    <li><a>July, 24 2014</a><br>Lorem Ipsum is simply dummy text of the printing and typesetting...</li>
  </ul>
  <a class="readmore" style="padding-left:10px">Read more...</a>
</section>

<div class="abs clients"></div>
<svg class="abs" style="left:93px;top:813px" width="10" height="18"><path d="M9 1 1 9l8 8" fill="none" stroke="#aaa" stroke-width="1.5"/></svg>
<svg class="abs" style="left:701px;top:813px" width="10" height="18"><path d="M1 1l8 8-8 8" fill="none" stroke="#aaa" stroke-width="1.5"/></svg>
<div class="abs client" style="left:115px">Halvern</div>
<div class="abs client" style="left:274px">Corvane</div>
<div class="abs client" style="left:410px">Tenmark Systems</div>
<div class="abs client" style="left:550px">Brightwell</div>

<div class="abs tweet"></div>
<div class="abs tweet-handle">@LarkstoneDeals</div>
<span class="abs tweet-icon"></span>
<p class="abs tweet-body">Lorem Ipsum is simply dummy text of the printing and typesetting industry. Lorem Ipsum has been the industry's standard dummy text ever since the 1500s...<a style="color:var(--link)">lnk.example/q7Rk</a></p>
<div class="abs dots"><span></span><span></span><span></span><span></span><span></span></div>

<footer class="abs footer"></footer>
<div class="abs vline" style="left:324px"></div>
<div class="abs vline" style="left:483px"></div>
<div class="abs col-h" style="left:93px;top:1005px">Newsletter!</div>
<div class="abs" style="left:94px;top:1026px;color:#d6deed">Subscribe to our M&amp;A Quarterly Updates</div>
<div class="abs email"><span>Enter email</span><b><svg width="16" height="11" viewBox="0 0 16 11"><rect x=".5" y=".5" width="15" height="10" fill="#fff"/><path d="M.5.5 8 6l7.5-5.5" fill="none" stroke="#0492cd"/></svg>Send</b></div>
<div class="abs col-h" style="left:347px;top:1005px">Follow Us</div>
<div class="abs social"><span>FB</span><span>TW</span><span>IN</span><span><svg width="11" height="8" viewBox="0 0 11 8"><rect x=".5" y=".5" width="10" height="7" fill="none" stroke="#fff"/><path d="M.5.5 5.5 4.5 10.5.5" fill="none" stroke="#fff"/></svg></span></div>
<div class="abs col-h" style="left:510px;top:1005px">Contact Us</div>
<address class="abs contact" style="font-style:normal">Larkstone Capital Partners, LLC<br>2140 Alder Crest Ave, Suite 310 Los Angeles,<br>CA 90024 United States of America<br>Mobile: +1 (555) 014-2290<br>EMail: <a>mergers@larkstonecapitalpartners.example</a></address>
<nav class="abs footnav"><a>Home</a><a>About</a><a>Services</a><a>Transactions</a><a>Research</a><a>Private Equity</a><a>Recommendations</a><a>About the Founder</a><a>Careers</a><a>News &amp; Blog</a></nav>
<div class="abs fline"></div>
<div class="abs copy">Copyright © 2014 Larkstone Capital Partners. All Rights Reserved.</div>
</body>
</html>
```